Business Card Design - Law Firm

We are a boutique law firm located near the beach in Manly, Australia. We have recently had a new logo designed and are revamping our business cards with the new logo.

We have recently had a business card design done for us but are not entirely happy with it. We are looking for something modern, simplistic but striking. We would like to see multiple designs.

We have attached a word document which includes our new logo and the current business card design which we are looking at moving away from.

We would like the business cards to be double sided. We would like the design to include something which we can print in gloss colour when we send it to the business card printers.

```html
<!DOCTYPE html>
<html lang="en">
<head>
<meta charset="utf-8">
<title>Calder &amp; Associates – Business Card</title>
<link rel="stylesheet" href="https://fonts.googleapis.com/css2?family=Montserrat:wght@400;500;600&display=swap">
<style>
  :root {
    --bg: #ecfccd;
    --card-light: #f4f3f2;
    --card-dark: #1b1e23;
    --violet: #6a6cb3;
    --ink: #15161a;
    --mark-grey: #8b8e94;
    --white: #ffffff;
  }
  * { box-sizing: border-box; margin: 0; padding: 0; }
  html, body { width: 1200px; height: 960px; overflow: hidden; }
  body {
    background: var(--bg);
    font-family: "Montserrat", sans-serif;
    position: relative;
  }
  .card {
    position: absolute;
    left: 240px;
    width: 720px;
    height: 412px;
    border-radius: 26px;
    box-shadow: 0 10px 24px rgba(60, 80, 20, 0.25);
    overflow: hidden;
  }
  .card--back { top: 45px; background: var(--card-dark); display: flex; align-items: center; justify-content: center; }
  .card--front { top: 503px; background: var(--card-light); }

  .back-mark {
    color: var(--mark-grey);
    font-size: 40px;
    font-weight: 500;
    letter-spacing: 2px;
  }

  .holder { position: absolute; left: 38px; top: 34px; }
  .holder__name {
    display: flex; align-items: center; gap: 14px;
    color: var(--violet); font-size: 30px; font-weight: 500; letter-spacing: 2px;
    word-spacing: 14px;
  }
  .holder__role {
    margin: 2px 0 0 74px;
    color: var(--ink); font-size: 15px; font-weight: 500; letter-spacing: 2.5px; word-spacing: 12px;
  }

  .firm-name {
    position: absolute; right: 34px; top: 120px;
    color: var(--violet); font-size: 25px; font-weight: 600; letter-spacing: 1.5px;
  }

  .web-band {
    position: absolute; left: 340px; right: 0; top: 178px; height: 56px;
    background: var(--card-dark);
    display: flex; align-items: center; gap: 14px; padding-left: 26px;
    color: var(--white); font-size: 15px; font-weight: 500; letter-spacing: 0.6px;
    white-space: nowrap;
  }
  .web-band svg { flex: 0 0 28px; }

  .contacts { position: absolute; left: 366px; top: 262px; list-style: none; }
  .contacts li {
    display: flex; align-items: center; gap: 18px;
    color: var(--ink); font-size: 14px; font-weight: 600; letter-spacing: 0.5px;
    margin-bottom: 18px; line-height: 1.15; white-space: nowrap;
  }
  .contacts svg { flex: 0 0 26px; }
</style>
</head>
<body>

<section class="card card--back" aria-label="Card back">
  <p class="back-mark">Calder &amp; Associates</p>
</section>

<section class="card card--front" aria-label="Card front">
  <div class="holder">
    <h1 class="holder__name">
      <svg width="30" height="30" viewBox="0 0 30 30" aria-hidden="true">
        <circle cx="18" cy="8" r="6" fill="var(--violet)"/>
        <path d="M2 28c0-9 6-13 14-13s12 4 12 13z" fill="var(--violet)"/>
      </svg>
      Maren Holloway
    </h1>
    <p class="holder__role">prectice manager</p>
  </div>

  <p class="firm-name">Calder &amp; Associates</p>

  <div class="web-band">
    <svg width="28" height="28" viewBox="0 0 28 28" aria-hidden="true">
      <circle cx="14" cy="14" r="12" fill="none" stroke="var(--violet)" stroke-width="2.5"/>
      <ellipse cx="14" cy="14" rx="5" ry="12" fill="none" stroke="var(--violet)" stroke-width="2"/>
      <path d="M2 10h24M2 18h24" stroke="var(--violet)" stroke-width="2"/>
    </svg>
    <span>www.calderandassociates.com.au</span>
  </div>

  <ul class="contacts">
    <li>
      <svg width="26" height="26" viewBox="0 0 26 26" aria-hidden="true">
        <path d="M6 2l4 1 2 6-3 2c1 3 3 5 6 6l2-3 6 2 1 4c-1 3-3 4-6 4C10 23 3 16 2 7c0-3 1-5 4-5z" fill="var(--violet)"/>
      </svg>
      <span>(02)-9000-4187</span>
    </li>
    <li>
      <svg width="26" height="20" viewBox="0 0 26 20" aria-hidden="true">
        <rect x="1" y="2" width="24" height="16" fill="none" stroke="var(--violet)" stroke-width="2"/>
        <path d="M1 2l12 10L25 2M1 18l9-8M25 18l-9-8" fill="none" stroke="var(--violet)" stroke-width="2"/>
      </svg>
      <span>maren.holloway@coveslaw.com.au</span>
    </li>
    <li>
      <svg width="26" height="30" viewBox="0 0 26 30" aria-hidden="true">
        <path d="M13 29C6 20 2 15 2 11a11 11 0 0 1 22 0c0 4-4 9-11 18z" fill="var(--violet)"/>
        <circle cx="13" cy="11" r="4" fill="var(--card-light)"/>
      </svg>
      <span>Suite 4,18 Tidewater Lane<br>Seacliff nsw 2099</span>
    </li>
  </ul>
</section>

</body>
</html>
```